Dryer Vent Cleaning Postcard Design

We need a postcard design for Duct Rangers, a company that specializes in dryer vent cleaning, repairs and upgrades. Dryer vents need periodic cleaning to avoid lint clogging, dryer malfunction, long dry times and even a house fire. This card will be sent to residential and businesses prospects to introduce them to our services and the importance of maintaining their dryer vents. Our website is @ ductranging.example and provides information about our services, photos of our work and our general color scheme (purple/orange). Final print size will be 5x7 horizontal.

Target Market(s)

homeowners and business owners (spas, salons, grooming, gyms, laundrymats, etc)

Requirements
Must have
• Reduce the risk of fire
shortened dry times
lower energy consumption
18000 dryer fires caused in the US per year
Nice to have
• Does your dryer take too long to dry?

```html
<!DOCTYPE html>
<html lang="en">
<head>
<meta charset="utf-8">
<title>Duct Rangers Postcard</title>
<link href="https://fonts.googleapis.com/css2?family=Catamaran:wght@500;600;700;800&family=Open+Sans:ital,wght@0,300;0,400;0,600;1,700&display=swap" rel="stylesheet">
<style>
  :root {
    --purple: #43306f;
    --purple-deep: #36265d;
    --purple-light: #5a4390;
    --orange: #f58a4b;
    --orange-red: #ef5a28;
    --lavender: #c7b7ef;
    --white: #ffffff;
    --bg: #ecebe8;
  }
  * { box-sizing: border-box; margin: 0; padding: 0; }
  html, body { width: 1200px; height: 840px; overflow: hidden; background: var(--bg); }
  body { position: relative; font-family: "Open Sans", sans-serif; }

  .card {
    position: absolute; width: 700px; height: 500px;
    transform: scale(0.82); transform-origin: top left;
    background: var(--purple); overflow: hidden;
    box-shadow: 0 4px 14px rgba(0,0,0,.18);
  }
  .card--front { left: 18px; top: 215px; }
  .card--back { left: 608px; top: 215px;
    background: radial-gradient(circle at 25% 20%, var(--purple-light), var(--purple) 55%, var(--purple-deep)); }

  .brand { position: absolute; display: flex; flex-direction: column; align-items: center; gap: 12px; }
  .brand__mark { width: 110px; height: 110px; border-radius: 50%; background: var(--orange); }
  .brand__name { font-family: "Catamaran", sans-serif; font-weight: 800; font-size: 28px; line-height: 32px; color: var(--white); letter-spacing: 1px; white-space: nowrap; }
  .card--front .brand { left: 50px; top: 50px; width: 230px; }
  .card--back .brand { left: 15px; top: 35px; width: 220px; }

  .pitch { position: absolute; left: 55px; top: 240px; width: 290px; }
  .pitch__head { font-family: "Catamaran", sans-serif; font-weight: 700; font-size: 19px; line-height: 22px; color: var(--orange); text-transform: uppercase; }
  .pitch__list { list-style: none; margin: 4px 0 14px; }
  .pitch__list li { color: var(--white); font-size: 16px; font-weight: 300; line-height: 21px; display: flex; align-items: center; gap: 6px; white-space: nowrap; }
  .pitch__list svg { width: 13px; height: 13px; flex: none; }

  .compare { position: absolute; top: 42px; width: 112px; height: 138px; }
  .compare--before { left: 420px; } .compare--after { left: 546px; }
  .compare__label { height: 22px; background: var(--orange-red); color: var(--white); font-size: 10px; font-weight: 600; text-align: center; line-height: 22px; letter-spacing: .5px; }
  .compare__photo { height: 116px; }
  .compare--before .compare__photo { background: radial-gradient(circle at 50% 45%, #3a3a3a 8%, #8f9090 30%, #b8b6ad 70%); }
  .compare--after .compare__photo { background: radial-gradient(circle at 50% 45%, #050505 12%, #555 45%, #a9a9a9 90%); }

  .dryer-art { position: absolute; left: 340px; top: 190px; width: 360px; height: 260px;
    background: linear-gradient(160deg, var(--purple) 0%, #8d78c8 35%, var(--lavender) 70%); }

  .band { position: absolute; left: 0; bottom: 0; width: 700px; height: 100px; }
  .band__url { position: absolute; left: 0; right: 0; bottom: 10px; text-align: center; font-style: italic; font-weight: 700; font-size: 22px; letter-spacing: 3px; color: var(--white); white-space: nowrap; }

  .contact { position: absolute; left: 22px; top: 222px; list-style: none; }
  .contact li { color: var(--white); font-size: 16px; font-weight: 300; line-height: 22px; display: flex; align-items: center; gap: 6px; white-space: nowrap; }
  .contact svg { width: 11px; height: 11px; flex: none; }
  .follow { position: absolute; left: 22px; top: 292px; display: flex; align-items: center; gap: 5px;
    font-family: "Catamaran", sans-serif; font-weight: 600; font-size: 21px; line-height: 26px; color: var(--orange); white-space: nowrap; }
  .follow__dot { width: 20px; height: 20px; border-radius: 50%; border: 1.5px solid var(--white); }

  .invite { position: absolute; left: 264px; top: 14px; width: 430px; font-size: 21px; line-height: 26px; color: var(--white); font-weight: 400; white-space: nowrap; }
  .invite em { font-style: normal; color: var(--orange); }

  .title-bar { position: absolute; left: 247px; top: 101px; width: 427px; height: 40px; background: var(--orange-red);
    color: var(--white); font-family: "Catamaran", sans-serif; font-weight: 600; font-size: 25px; text-align: center; line-height: 42px; white-space: nowrap; }

  .service { position: absolute; width: 200px; }
  .service__photo { height: 118px; }
  .service__label { height: 31px; background: var(--orange-red); color: var(--white); font-size: 13px; font-weight: 600; text-align: center; line-height: 31px; white-space: nowrap; }
  .s1 { left: 247px; top: 152px; } .s2 { left: 476px; top: 152px; }
  .s3 { left: 20px; top: 328px; } .s4 { left: 247px; top: 328px; } .s5 { left: 478px; top: 328px; }
  .s1 .service__photo { background: linear-gradient(180deg, #e9e9e9 40%, #9a9a96 85%, #3c3c3c); }
  .s2 .service__photo { background: linear-gradient(135deg, #d8c8a8, #8a7058 50%, #a6a2a0); }
  .s3 .service__photo { background: linear-gradient(90deg, #6a6a6a, #b9b9b9 45%, #d8d8d8); }
  .s4 .service__photo { background: linear-gradient(180deg, #8b3b2f, #a7523f 55%, #e6e6e6); }
  .s5 .service__photo { background: linear-gradient(180deg, #e6eaf0 30%, #6a4a38 75%, #2c2c2c); }
</style>
</head>
<body>

<section class="card card--front" aria-label="Postcard front">
  <div class="brand">
    <div class="brand__mark"></div>
    <div class="brand__name">DUCT RANGERS</div>
  </div>

  <div class="pitch">
    <h2 class="pitch__head">18000 dryer fires<br>caused in the US per year</h2>
    <ul class="pitch__list">
      <li><svg viewBox="0 0 12 12"><path d="M1 6.5l3 3 7-8" fill="none" stroke="#f58a4b" stroke-width="1.6"/></svg>Reduce the risk of fire</li>
    </ul>
    <h2 class="pitch__head">Does your dryer<br>take too long to dry?</h2>
    <ul class="pitch__list">
      <li><svg viewBox="0 0 12 12"><path d="M1 6.5l3 3 7-8" fill="none" stroke="#f58a4b" stroke-width="1.6"/></svg>Shortened dry times</li>
      <li><svg viewBox="0 0 12 12"><path d="M1 6.5l3 3 7-8" fill="none" stroke="#f58a4b" stroke-width="1.6"/></svg>Lower energy consumption</li>
    </ul>
  </div>

  <div class="compare compare--before">
    <div class="compare__label">BEFORE</div>
    <div class="compare__photo" role="img" aria-label="Photo of a lint-clogged dryer duct before cleaning"></div>
  </div>
  <div class="compare compare--after">
    <div class="compare__label">AFTER</div>
    <div class="compare__photo" role="img" aria-label="Photo of a clean dryer duct after cleaning"></div>
  </div>

  <div class="dryer-art" role="img" aria-label="Line illustration of a dryer with lint bursting from the top"></div>

  <svg class="band" viewBox="0 0 700 100" preserveAspectRatio="none">
    <path d="M0 0 Q350 80 700 0 L700 100 L0 100 Z" fill="#f58a4b"/>
    <path d="M0 0 Q350 80 700 0" fill="none" stroke="#ef5a28" stroke-width="4"/>
    <path d="M0 98 H700" stroke="#ef5a28" stroke-width="5"/>
  </svg>
  <div class="band__url">www.DuctRangers.example</div>
</section>

<section class="card card--back" aria-label="Postcard back">
  <div class="brand">
    <div class="brand__mark"></div>
    <div class="brand__name">DUCT RANGERS</div>
  </div>

  <ul class="contact">
    <li><svg viewBox="0 0 12 12"><path d="M2 1l2.5 0 1 3-1.5 1a7 7 0 0 0 3 3l1-1.5 3 1V10a1.5 1.5 0 0 1-1.5 1.5A9.5 9.5 0 0 1 .5 2.5 1.5 1.5 0 0 1 2 1z" fill="#f58a4b"/></svg>+1 555 010 8001</li>
    <li><svg viewBox="0 0 12 12"><rect x="1" y="2.5" width="10" height="7" fill="#f58a4b"/><path d="M1 2.5l5 4 5-4" fill="none" stroke="#43306f" stroke-width="1"/></svg>office@ductranging.example</li>
    <li><svg viewBox="0 0 12 12"><circle cx="6" cy="6" r="5" fill="#f58a4b"/></svg>www.ductranging.example</li>
  </ul>
  <div class="follow">Follow Us :
    <span class="follow__dot"></span><span class="follow__dot"></span><span class="follow__dot"></span><span class="follow__dot"></span>
  </div>

  <p class="invite">Feel free to <em>give us a call</em><br>contact us through our online form or<br><em>schedule your appointment online!</em></p>

  <div class="title-bar">Duct Rangers - Dryer Vent Cleaning</div>

  <div class="service s1">
    <div class="service__photo" role="img" aria-label="Photo of lint pulled from a dryer vent"></div>
    <div class="service__label">Dryer Vent Cleaning</div>
  </div>
  <div class="service s2">
    <div class="service__photo" role="img" aria-label="Photo of a newly installed metal dryer duct"></div>
    <div class="service__label">Dryer Vent Installation</div>
  </div>
  <div class="service s3">
    <div class="service__photo" role="img" aria-label="Photo of a flexible foil duct behind a dryer"></div>
    <div class="service__label">Professional Dryer Installation</div>
  </div>
  <div class="service s4">
    <div class="service__photo" role="img" aria-label="Photo of a white vent cap on a brick wall"></div>
    <div class="service__label">Vent Cap Replacement</div>
  </div>
  <div class="service s5">
    <div class="service__photo" role="img" aria-label="Photo of a bird nest pulled from an exterior vent"></div>
    <div class="service__label">Bird Nest Removal</div>
  </div>
</section>

</body>
</html>
```